Business Card Design Project

Velvet Harbor is a Boutique Clothing. On the business cards I would like to have this included
Website: www.velvetharbor-example.com
Email: shop@velvetharbor-example.com
Owner: Mai Torres & Bo Rinaldi

Industry/Entity Type

Business

Contact Information for Business Card

I wanted something simple and elegant. I have attach business logo.

```html
<!DOCTYPE html>
<html lang="en">
<head>
<meta charset="UTF-8">
<title>Velvet Harbor — Business Cards</title>
<link rel="stylesheet" href="https://fonts.googleapis.com/css2?family=Oswald:wght@600&family=Roboto:wght@300;400&display=swap">
<style>
  :root {
    --bg: #2a2d31;
    --card: #141414;
    --card-edge: #1d1d1d;
    --silver: #d6d6d6;
    --silver-soft: #8e8e8e;
    --silver-dim: #6a6a6a;
  }
  * { box-sizing: border-box; margin: 0; padding: 0; }
  html, body {
    width: 1200px;
    height: 900px;
    overflow: hidden;
    background: var(--bg);
  }
  .sheet {
    width: 1200px;
    height: 900px;
    display: flex;
    align-items: center;
    justify-content: center;
    gap: 60px;
  }
  .card {
    width: 525px;
    height: 300px;
    background: var(--card);
    border: 1px solid var(--card-edge);
    border-radius: 26px;
    box-shadow: 0 18px 40px rgba(0,0,0,0.45);
    display: flex;
    flex-direction: column;
    align-items: center;
    justify-content: center;
  }

  /* Contact side */
  .contact-card { text-align: center; }
  .owners {
    font-family: "Oswald", sans-serif;
    font-weight: 600;
    font-size: 30px;
    letter-spacing: 0.5px;
    text-transform: uppercase;
    color: var(--silver);
  }
  .role {
    font-family: "Roboto", sans-serif;
    font-weight: 300;
    font-size: 17px;
    color: var(--silver-dim);
    margin-top: 2px;
  }
  .contact-icons {
    display: flex;
    gap: 8px;
    margin: 12px 0 10px;
  }
  .contact-icons svg { width: 13px; height: 13px; fill: none; stroke: var(--silver-soft); stroke-width: 1.6; }
  .contact-list {
    list-style: none;
    font-family: "Roboto", sans-serif;
    font-weight: 300;
    font-size: 19px;
    line-height: 1.3;
    color: var(--silver-soft);
  }

  /* Brand side */
  .brand-card { gap: 16px; }
  .brand-dot {
    width: 10px;
    height: 10px;
    border-radius: 50%;
    background: var(--silver);
  }
  .brand-name {
    font-family: "Roboto", sans-serif;
    font-weight: 300;
    font-size: 30px;
    letter-spacing: 9px;
    text-transform: uppercase;
    color: var(--silver);
  }
</style>
</head>
<body>
  <main class="sheet">
    <section class="card contact-card">
      <h1 class="owners">Mai Torres &amp; Bo Rinaldi</h1>
      <p class="role">Owner</p>
      <div class="contact-icons" aria-hidden="true">
        <svg viewBox="0 0 16 16"><path d="M4 2l2.5 3-1.5 1.5a8 8 0 0 0 4.5 4.5L11 9.5l3 2.5-1.5 2A10 10 0 0 1 2 3.5z"/></svg>
        <svg viewBox="0 0 16 16"><rect x="2" y="4" width="12" height="8" rx="1"/><path d="M2 4l6 5 6-5"/></svg>
        <svg viewBox="0 0 16 16"><circle cx="8" cy="8" r="6"/><path d="M2 8h12M8 2c3 3 3 9 0 12M8 2c-3 3-3 9 0 12"/></svg>
      </div>
      <ul class="contact-list">
        <li>(555) 014-2290</li>
        <li>shop@velvetharbor-example.com</li>
        <li>www.velvetharbor-example.com</li>
      </ul>
    </section>

    <section class="card brand-card">
      <span class="brand-dot" aria-hidden="true"></span>
      <p class="brand-name">Velvet Harbor</p>
    </section>
  </main>
</body>
</html>
```